Hochzeitseinladung
Zielgruppe
Gastronomie - Zielgruppe ist ein Hochzeitspaar, welches bei uns feiert. Wir dürfen Ihre Hochzeitseinladung entwerfen.
Aufgabenstellung
Den Textvorschlag des Brautpaares findet Ihr im Anhang. Das Thema der Hochzeit ist AMORE.
1. Die Hochzeitseinladung darf gerne kreativ gestaltet sein, vielleicht in Form des Moodboard-Bildes im Anhang? Mattes hat braune Haare und Locken und Doreen lange braune Haare. Beide tragen eine Brille.
Das Hochzeitspaar hat noch einen kleinen braunen Zwergpudel 'Fips', vielleicht findet er auch noch Platz auf der Einladungskarte ;-).
2. Als Alternativ-Vorschlag wäre ein klassisches Design auf zB geprägtem Papier toll.
3. Etwas Schlichtes mit einem Neon-Accessoire würde das Hochzeitspaar auch gut finden. Zb brauner Karton mit einem Neonband.

```html
<!DOCTYPE html>
<html lang="de">
<head>
<meta charset="utf-8">
<title>Hochzeitseinladung Doreen &amp; Mattes</title>
<link href="https://fonts.googleapis.com/css2?family=Allura&family=Mrs+Saint+Delafield&family=Cormorant+Garamond:wght@400;500;600&family=Cinzel:wght@400&display=swap" rel="stylesheet">
<style>
  :root {
    --backdrop: #e4e4e2;
    --paper: #fdfbf5;
    --gold: #c9a24f;
    --gold-soft: #e8c46a;
    --ink: #4a4640;
    --ink-soft: #6d675e;
    --blush: #ecdccd;
    --blush-deep: #e3cdb9;
    --sage: #a9b59a;
    --leaf: #7d925f;
    --line: #2d2b28;
  }
  * { box-sizing: border-box; margin: 0; padding: 0; }
  html, body { width: 1200px; height: 856px; overflow: hidden; }
  body { background: var(--backdrop); position: relative; font-family: "Cormorant Garamond", serif; color: var(--ink); }

  .card {
    position: absolute; top: 88px; width: 480px; height: 680px;
    background: var(--paper); box-shadow: 0 6px 18px rgba(0,0,0,.12);
    overflow: hidden;
  }
  .card--invite { left: 90px; }
  .card--details { left: 630px; }

  .floral { position: absolute; border-radius: 50%; }
  .floral--blossom {
    background: radial-gradient(closest-side, rgba(227,205,185,.9) 0%, rgba(236,220,205,.75) 35%, rgba(214,220,200,.45) 65%, rgba(253,251,245,0) 100%);
  }
  .floral--leaves {
    background: radial-gradient(closest-side, rgba(125,146,95,.7) 0%, rgba(169,181,154,.5) 45%, rgba(253,251,245,0) 100%);
  }

  /* Einladung */
  .invite__kicker { position: absolute; top: 120px; width: 100%; text-align: center; font-family: "Cinzel", serif; font-size: 12px; letter-spacing: .3em; color: var(--ink); }
  .invite__names { position: absolute; top: 145px; width: 100%; text-align: center; font-family: "Mrs Saint Delafield", cursive; font-weight: 400; font-size: 64px; color: var(--gold); line-height: 1.2; }
  .invite__line { position: absolute; top: 238px; width: 100%; text-align: center; font-family: "Cinzel", serif; font-size: 11px; letter-spacing: .22em; line-height: 1.6; color: var(--ink); }
  .invite__facts { position: absolute; top: 286px; left: 40px; right: 40px; display: flex; justify-content: space-between; align-items: flex-end; }
  .fact { text-align: center; font-size: 14px; color: var(--ink); width: 110px; }
  .fact svg { display: block; margin: 0 auto 6px; }
  .fact--motto { font-family: "Mrs Saint Delafield", cursive; font-size: 46px; color: var(--line); line-height: 1; width: 160px; }
  .invite__scene {
    position: absolute; left: 70px; right: 70px; bottom: 0; height: 300px;
    border-radius: 170px 170px 0 0;
    background: linear-gradient(180deg, #f0e0b5 0%, #f2e7cf 35%, #d9dde0 75%, #b9c4cc 100%);
    border: 6px solid var(--gold-soft); border-bottom: none;
  }

  /* Details */
  .details__title { position: absolute; top: 48px; width: 100%; text-align: center; font-family: "Mrs Saint Delafield", cursive; font-weight: 400; font-size: 88px; color: var(--gold); line-height: 1.1; }
  .details__sub { position: absolute; top: 150px; width: 100%; text-align: center; font-size: 13px; letter-spacing: .08em; color: var(--ink-soft); }
  .timeline { position: absolute; top: 205px; left: 40px; right: 40px; }
  .timeline__rule { position: absolute; top: 62px; left: 48px; right: 48px; height: 1.5px; background: var(--line); }
  .timeline__steps { display: flex; justify-content: space-between; }
  .step { width: 100px; text-align: center; position: relative; }
  .step svg { display: block; margin: 0 auto; height: 48px; }
  .step__dot { width: 9px; height: 9px; border-radius: 50%; background: var(--line); margin: 9px auto 8px; }
  .step__time { font-size: 13px; font-weight: 500; color: var(--ink); }
  .step__what { font-size: 9px; letter-spacing: .06em; line-height: 1.35; color: var(--ink-soft); text-transform: uppercase; }

  .section__head { position: absolute; width: 100%; text-align: center; font-family: "Mrs Saint Delafield", cursive; font-weight: 400; font-size: 40px; color: var(--gold); line-height: 1.1; }
  .section__body { position: absolute; left: 40px; right: 40px; text-align: center; font-size: 12.5px; line-height: 1.45; color: var(--ink-soft); }
</style>
</head>
<body>

<section class="card card--invite" aria-label="Einladungskarte">
  <div class="floral floral--blossom" style="left:-60px;top:70px;width:200px;height:240px" role="img" aria-label="Aquarellblüten in Creme und Rosé mit Blättern"></div>
  <div class="floral floral--blossom" style="right:-50px;top:-40px;width:210px;height:230px" role="img" aria-label="Aquarellblüten in Creme und Rosé mit Blättern"></div>

  <p class="invite__kicker">WE SAY YES</p>
  <h1 class="invite__names">Doreen &amp; Mattes</h1>
  <p class="invite__line">INVITE YOU TO JOIN THEIR WEDDING<br>CELEBRATION ON</p>

  <div class="invite__facts">
    <div class="fact">
      <svg width="24" height="24" viewBox="0 0 24 24" fill="none" stroke="#c9a24f" stroke-width="1.6"><rect x="3" y="5" width="18" height="16" rx="2"/><path d="M3 10h18M8 3v4M16 3v4"/><path d="M7 14h2M11 14h2M15 14h2M7 17h2M11 17h2" stroke-width="1.4"/></svg>
      20.04.2024
    </div>
    <div class="fact fact--motto">Amor</div>
    <div class="fact">
      <svg width="28" height="28" viewBox="0 0 28 28"><circle cx="14" cy="14" r="12.5" fill="none" stroke="#c9a24f" stroke-width="1.4"/><path d="M7 14.5 14 8l7 6.5h-2V20h-3.5v-3.5h-3V20H9v-5.5z" fill="#c9a24f"/></svg>
      Münster
    </div>
  </div>

  <div class="invite__scene" role="img" aria-label="Illustration: Brautpaar von hinten unter einem goldenen Blumenbogen mit Vorhängen"></div>
  <div class="floral floral--leaves" style="left:10px;bottom:-30px;width:130px;height:180px" role="img" aria-label="Grüne Zweige mit Gänseblümchen"></div>
  <div class="floral floral--leaves" style="right:0;bottom:50px;width:130px;height:180px" role="img" aria-label="Grüne Zweige mit Gänseblümchen"></div>
</section>

<section class="card card--details" aria-label="Detailkarte">
  <div class="floral floral--blossom" style="left:-50px;top:-40px;width:190px;height:250px" role="img" aria-label="Aquarellblüten in Creme und Rosé mit Blättern"></div>
  <div class="floral floral--blossom" style="right:-50px;top:-40px;width:190px;height:250px" role="img" aria-label="Aquarellblüten in Creme und Rosé mit Blättern"></div>

  <h2 class="details__title">Details</h2>
  <p class="details__sub">ZEITPLAN FÜR UNSERE HOCHZEIT</p>

  <div class="timeline">
    <div class="timeline__rule"></div>
    <div class="timeline__steps">
      <div class="step">
        <svg viewBox="0 0 48 48" fill="none" stroke="#4a4640" stroke-width="1.4"><path d="M24 2v6M21 5h6M20 14l4-6 4 6v8h-8zM6 44V30l14-8h8l14 8v14zM4 44h40"/><path d="M20 44v-7a4 4 0 0 1 8 0v7M11 34h3v4h-3zM34 34h3v4h-3z"/></svg>
        <div class="step__dot"></div>
        <div class="step__time">13:30 Uhr</div>
        <div class="step__what">Standesamt<br>Lindenhof<br>Kloster</div>
      </div>
      <div class="step">
        <svg viewBox="0 0 48 48" fill="none" stroke="#4a4640" stroke-width="1.4"><path d="M10 14l10-3 3 10a6 6 0 0 1-11 3zM38 14l-10-3-3 10a6 6 0 0 0 11 3z"/><path d="M17 27l3 11M14 39l7-2M31 27l-3 11M34 39l-7-2"/><path d="M24 8c-2-3-6 0-0 4 6-4 2-7 0-4z"/></svg>
        <div class="step__dot"></div>
        <div class="step__time">14:30 UHR</div>
        <div class="step__what">Sektempfang<br>Rosengarten</div>
      </div>
      <div class="step">
        <svg viewBox="0 0 48 48" fill="none" stroke="#4a4640" stroke-width="1.4"><path d="M20 38A16 16 0 1 1 36 20"/><path d="M20 12v10l6 3"/><path d="M24 28h18v8a7 7 0 0 1-7 7h-4a7 7 0 0 1-7-7zM42 31h3a3 3 0 0 1 0 6h-3"/><path d="M30 20c-1 2 1 3 0 5M35 20c-1 2 1 3 0 5"/></svg>
        <div class="step__dot"></div>
        <div class="step__time">AB 16:00 UHR</div>
        <div class="step__what">Kurze Pause</div>
      </div>
      <div class="step">
        <svg viewBox="0 0 48 48" fill="none" stroke="#4a4640" stroke-width="1.4"><circle cx="24" cy="26" r="13"/><circle cx="24" cy="26" r="8"/><path d="M6 10c-3 4-2 10 2 11v19M42 8v8a3 3 0 0 1-6 0V8M39 8v32"/></svg>
        <div class="step__dot"></div>
        <div class="step__time">18:30UHR</div>
        <div class="step__what">Einfinden im<br>Gasthaus<br>Alter<br>Mühlenhof</div>
      </div>
    </div>
  </div>

  <h3 class="section__head" style="top:400px">Standesamt</h3>
  <p class="section__body" style="top:450px">Im Standesamt stehen leider nur 20 Plätze zur Verfügung. Falls Ihr Interesse habt, freue ich mich über Eure Nachricht, damit wir gemeinsam eine Lösung finden können.</p>

  <h3 class="section__head" style="top:540px">Dresscodes</h3>
  <p class="section__body" style="top:590px">Tagsüber : Cocktail<br>Abends: Festlich elegant &amp; dunkler Anzug</p>

  <div class="floral floral--leaves" style="left:-30px;bottom:-30px;width:140px;height:190px" role="img" aria-label="Grüne Aquarellzweige"></div>
  <div class="floral floral--leaves" style="right:-30px;bottom:-30px;width:140px;height:190px" role="img" aria-label="Grüne Aquarellzweige"></div>
</section>

</body>
</html>
```